Blogging Platform for Christian Missions

We need the main (one) page design for FaithPostly. FaithPostly is a blogging platform for people (missionaries) who work for Christian Mission organisations in various countries. It will provides an easy way for them to setup and maintain a blog that will have features specifically for missions.

There's a lot of work involved in creating a web page design so I am happy to receive many quick rough designs. I will select my favourite four or five designs and these can submit the full design.

Please see the attached wireframe. Please also see the attached logo.

Main colours
- black
- white
- grey
- red (see logo colour) can be used occasionally eg. titles
- another complementary colour - occasionally used

Photos uploaded by the missionaries will provide colour for the website.

It needs to be a clean design that is not cluttered. The main focus are the blog posts. The information on the side complements the blog. There are navigational options at the top and bottom. The FaithPostly logo is not the main focus. The person's name (blog owner) is what needs to be most prominent.

I love the BrightNoma design (http://www.brightnoma-demo.net/). I particularly like the soft design - light grey background, white background boxes for content. The focus is the content - text and photos. I also like the subtle use of breakout image - "Step into the Venture". I like the black navigation header and the black footer. I do not want a exact copy of the site but I'd like to use this concept .

I also like this Quibbly design (http://calm.quibbly-demo.net/theme/preview/5193) because of the white box (and the shadow) for the content. I also like how the word "Quote" and the number of "notes" breaks out of the white content area (see attachment). I'd like to do this, if possible with the date. This is just a "nice to have" - definitely not essential. I don't like the font for the title in this example.

We have build a simple prototype already. I cautiously show this because I want the the design of this to be completely ignored. I used a free template. Along with the wireframe this prototype should an idea of what kind of content will be displayed but please don't look too much at it.
http://faithpostly-demo.org/blog/1

The design will be used to create a website using Verdant. We will use zScript so feel free to suggest an animation or lightbox effect to make your design more dynamic. This is a nice to have.

Once we have our final design we will need to define the style for:
- h1 through h4 tags
- Paragraphs
- Lists
- Block quotes
- Italics, bolding and underlining
- Links, including active, hover and visited states

Please let me know what additional information you need. Also let me know if there is something I have not considered.

Target Market(s)

The target customers are mission workers aged 25-35 who will post blog entries. These posts will be read by their friends and family.

Requirements
Must have
• Clean simple design. Must be inspired by the BrightNoma (http://www.brightnoma-demo.net/) design without copying it.
Nice to have
• Design element that breaks out of the boxes. See the screenshot attached from the Quibbly site. Described more in the project overview.
Should not have
• Should not use fonts that are not web-friendly. Should not have features that will be difficult to implement using HTML/CSS.

```html
<!DOCTYPE html>
<html lang="en">
<head>
<meta charset="utf-8">
<title>FaithPostly – Hannah Brooks</title>
<link rel="stylesheet" href="https://fonts.googleapis.com/css2?family=PT+Sans:wght@400;700&display=swap">
<style>
:root{
  --red:#d9112b;
  --pink:#f5a3ae;
  --black:#000;
  --ink:#111;
  --grey:#777;
  --line:#cfcfcf;
  --page:#efeeec;
  --white:#fff;
  --link:#1a3fc4;
}
*{box-sizing:border-box;margin:0;padding:0}
html,body{width:820px;height:1200px;overflow:hidden}
body{position:relative;background:var(--page);font-family:"PT Sans",Arial,sans-serif;color:var(--ink);font-size:11px;line-height:1.3}
a{color:var(--link)}
.abs{position:absolute}

/* top navigation */
.topnav{left:0;top:0;width:820px;height:26px;background:var(--black)}
.topnav ul{list-style:none;display:flex;height:26px;align-items:center;padding-left:14px;gap:0}
.topnav li a{color:var(--white);text-decoration:none;font-size:11.5px;padding:5px 8px;margin-right:9px}
.topnav li a.active{background:var(--red)}
.search{right:24px;top:5px;display:flex;align-items:center;gap:8px;color:var(--white);font-size:11px}
.search .field{width:96px;height:14px;background:var(--white);position:relative}

/* header */
.brand{left:16px;top:42px;width:360px;height:66px}
.brand .mark{position:absolute;left:0;top:6px;width:44px;height:44px;border-radius:50%;background:var(--red)}
.brand .name{position:absolute;left:82px;top:4px;font-size:34px;color:#666;letter-spacing:-0.5px}
.brand .tag{position:absolute;left:84px;top:44px;font-size:13px;color:var(--red)}

.signin{left:541px;top:37px;width:150px}
.signin h2,.register h2{font-weight:400;color:var(--red);font-size:16px}
.signin .row{display:flex;align-items:center;font-size:8.5px;margin-top:9px}
.signin .row span{width:44px}
.signin .row i{display:block;width:94px;height:14px;border:1px solid var(--line);background:var(--white)}
.signin .opts{display:flex;align-items:center;gap:6px;font-size:8.5px;margin-top:10px}
.signin .dot{width:11px;height:11px;border:1px solid #999;border-radius:50%;background:var(--white)}
.signin .btn{margin-left:14px;border:1px solid #999;border-radius:7px;padding:1px 9px;background:#f3f3f3}
.signin .forgot{font-size:8.5px;margin:8px 0 0 26px}
.register{left:700px;top:37px;width:110px}
.register p{font-size:8.5px;line-height:1.25;margin-top:8px}
.register .now{display:flex;align-items:center;gap:5px;color:var(--red);font-size:12px;margin:14px 0 0 10px}
.register .now i{display:block;width:14px;height:14px;border-radius:50%;background:var(--red);position:relative}
.register .now i::after{content:"";position:absolute;left:5px;top:3px;border-left:6px solid var(--white);border-top:4px solid transparent;border-bottom:4px solid transparent}

.owner{left:29px;top:130px}
.owner h1{font-weight:400;color:var(--red);font-size:28px;line-height:1}
.owner p{font-size:12px;margin-top:2px}
.follow{left:421px;top:135px;width:90px;font-size:10px;text-align:right}
.follow .icons{display:flex;gap:4px;margin-top:3px;justify-content:flex-end}
.icon{width:24px;height:24px;border-radius:4px}
.icon.mail{background:var(--white);border:1px solid #aaa}
.icon.blue{background:#3b5ea8}
.icon.sky{background:#4fb6e8}

/* main post column */
.posts{left:14px;top:184px;width:505px;height:868px;background:var(--white);border:1px solid var(--line);box-shadow:0 1px 4px rgba(0,0,0,.12)}
.post-date{width:31px;text-align:center;color:var(--white)}
.post-date .m{background:var(--grey);font-size:10px;height:17px;line-height:17px}
.post-date .d{background:var(--pink);font-size:19px;font-weight:700;height:26px;line-height:26px}
.post-date .y{background:var(--grey);font-size:9.5px;height:16px;line-height:16px}
.post-title{font-weight:400;font-size:28px;line-height:1}
.post-tools{display:flex;gap:3px}
.count{width:30px;height:24px;border:1px solid #ddd;border-radius:4px;background:#f4f4f8;color:#2a3bbf;font-weight:700;font-size:12px;text-align:center;line-height:22px}
.post-body{width:440px;font-size:11px;line-height:1.32}
.media{background:#e6e6e6}
.caption{font-style:italic;font-size:9px;text-align:center;width:270px}
.readmore{font-size:11px}
.ribbon{width:146px;height:28px;background:var(--red);color:var(--white);font-size:12.5px;line-height:28px;padding-left:20px;clip-path:polygon(0 0,100% 0,100% 100%,0 100%,10px 50%)}
.ribbon-tail{width:8px;height:8px;background:#8a0a1a;clip-path:polygon(0 0,100% 0,0 100%)}
.video{background:#fff;border:2px solid #333}
.video .screen{position:absolute;left:4px;top:4px;right:4px;bottom:18px;background:#f0f0f0}
.video .bar{position:absolute;left:0;right:0;bottom:0;height:16px;background:#ccc}
.note{font-style:italic;color:var(--link);font-size:10px}
.pager{display:flex;gap:5px}
.pager a{display:block;border:1px solid var(--red);color:var(--ink);text-decoration:none;font-size:11px;padding:3px 7px;background:var(--white)}
.pager a.current{background:var(--red);color:var(--white)}
.rss{width:22px;height:22px;border-radius:4px;background:#f08a24}

/* sidebar */
.side{left:541px;width:268px}
.side h3{font-weight:400;color:var(--red);font-size:12.5px;margin-bottom:6px}
.side p,.side li{font-size:10.5px;line-height:1.3}
.side ul{list-style:none}
.side .more{font-style:italic;font-size:10.5px;display:block;margin-top:6px}
.side .pic{background:#d2d2d2;border:2px solid #333;margin:0 auto 6px}

/* footer */
.footer{left:0;top:1068px;width:820px;height:94px;background:var(--black);color:var(--white)}
.footer .col{position:absolute;top:14px}
.footer h4{font-weight:400;font-size:12px;margin-bottom:6px}
.footer li{list-style:none;font-size:8.5px;line-height:1.25}
.footer .tab{position:absolute;right:0;top:8px;width:22px;height:78px;background:var(--red);color:var(--white);writing-mode:vertical-rl;font-size:10px;text-align:center;line-height:22px;border-radius:4px 0 0 4px}
.legal{left:0;top:1162px;width:820px;height:38px;display:flex;align-items:center;justify-content:center;gap:8px;font-size:9px;color:#333}
.legal .mini{display:flex;align-items:center;gap:4px;color:#666;font-size:13px}
.legal .mini i{width:14px;height:14px;border-radius:50%;background:var(--red);display:block}
</style>
</head>
<body>

<nav class="topnav abs">
  <ul>
    <li><a class="active" href="#">Home</a></li>
    <li><a href="#">Mission Blogs</a></li>
    <li><a href="#">Opportunities</a></li>
    <li><a href="#">Missionaries Forum</a></li>
    <li><a href="#">Contact Us</a></li>
  </ul>
</nav>
<div class="search abs"><span class="field"></span><span>Search</span></div>

<header>
  <div class="brand abs">
    <span class="mark"></span>
    <span class="name">faithpostly.org</span>
    <span class="tag">Read about Missions everywhere, right here (beta)</span>
  </div>

  <form class="signin abs">
    <h2>Sign In</h2>
    <div class="row"><span>Username:</span><i></i></div>
    <div class="row"><span>Password:</span><i></i></div>
    <div class="opts"><span class="dot"></span>Remember me<span class="btn">Login</span></div>
    <p class="forgot">Forgot Password? <a href="#">Here</a></p>
  </form>

  <div class="register abs">
    <h2>Register</h2>
    <p>Lorem ipsum dolor sit amet, maiores ornare ac fermentum, imperdiet ut vivamus a, nam lectus at nunc. Quam euismod sem, semper ut potenti pellentesque</p>
    <a class="now" href="#">register now <i></i></a>
  </div>

  <div class="owner abs">
    <h1>Hannah Brooks</h1>
    <p>Harvest Reach Australia</p>
  </div>
  <div class="follow abs">
    follow Hannah Brooks
    <div class="icons"><span class="icon mail"></span><span class="icon blue"></span><span class="icon sky"></span></div>
  </div>
</header>

<main>
  <section class="posts abs"></section>

  <!-- post one -->
  <div class="post-date abs" style="left:7px;top:199px"><div class="m">April</div><div class="d">14</div><div class="y">2011</div></div>
  <h2 class="post-title abs" style="left:54px;top:196px">Just Arrived</h2>
  <div class="post-tools abs" style="left:421px;top:198px"><span class="count">21</span><span class="icon blue"></span><span class="icon sky"></span></div>
  <p class="post-body abs" style="left:54px;top:231px">Lorem ipsum dolor sit amet, maiores ornare ac fermentum, imperdiet ut vivamus a, nam lectus at nunc. Quam euismod sem, semper ut potenti pellentesque quisque. In eget sapien sed, sit duis vestibulum ultricies, placerat morbi amet vel, nullam in in lorem vel. In molestie elit dui dictum, praesent nascetur pulvinar sed, in dolor pede in aliquam, risus nec error quis pharetra. Eros metus quam augue suspendisse, metus rutrum risus erat in.</p>
  <div class="media abs" role="img" aria-label="Photo of arrival at the mission field" style="left:152px;top:303px;width:230px;height:137px"></div>
  <p class="caption abs" style="left:132px;top:451px">just arrive image</p>
  <p class="post-body abs" style="left:54px;top:474px">In ultrices quo ut lectus, etiam vestibulum urna a est, pretium luctus euismod nisl, pellentesque turpis hac ridiculus massa. Venenatis a taciti dolor platea, curabitur lorem platea urna odio, convallis sit pellentesque lacus proin. Et ipsum velit diam nulla, fringilla vel tincidunt vitae, elit turpis tellus vivamus, dictum adipiscing convallis magna.</p>
  <a class="readmore abs" href="#" style="left:54px;top:531px">Read More</a>
  <div class="ribbon abs" style="left:382px;top:530px">Opportunities</div>
  <div class="ribbon-tail abs" style="left:520px;top:558px"></div>

  <!-- post two -->
  <span class="note abs" style="left:289px;top:590px">add new comment</span>
  <svg class="abs" style="left:370px;top:598px" width="56" height="28" viewBox="0 0 56 28"><line x1="1" y1="1" x2="54" y2="26" stroke="#1a3fc4" stroke-width="1"/></svg>
  <div class="post-date abs" style="left:7px;top:611px"><div class="m">June</div><div class="d">06</div><div class="y">2011</div></div>
  <h2 class="post-title abs" style="left:54px;top:608px">Resurrection Prayers</h2>
  <div class="post-tools abs" style="left:421px;top:611px"><span class="count">79</span><span class="icon blue"></span><span class="icon sky"></span></div>
  <p class="post-body abs" style="left:54px;top:644px">Lorem ipsum dolor sit amet, maiores ornare ac fermentum, imperdiet ut vivamus a, nam lectus at nunc. Quam euismod sem, semper ut potenti pellentesque quisque. In eget sapien sed, sit duis vestibulum ultricies, placerat morbi amet vel, nullam in in lorem vel. In molestie elit dui dictum, praesent nascetur pulvinar sed, in dolor pede in aliquam, risus nec error quis pharetra. Eros metus quam augue suspendisse, metus rutrum risus erat in.</p>
  <div class="video abs" style="left:159px;top:714px;width:213px;height:142px">
    <div class="screen"></div>
    <svg class="abs" style="left:88px;top:40px" width="36" height="40" viewBox="0 0 36 40"><polygon points="2,2 34,20 2,38" fill="#c9c9c9"/></svg>
    <div class="bar">
      <svg width="209" height="16" viewBox="0 0 209 16"><polygon points="6,4 12,8 6,12" fill="#333"/><line x1="20" y1="8" x2="185" y2="8" stroke="#333" stroke-width="2"/><circle cx="58" cy="8" r="5" fill="#fff" stroke="#333"/><rect x="192" y="5" width="4" height="6" fill="#333"/><polygon points="196,5 202,2 202,14 196,11" fill="#333"/></svg>
    </div>
  </div>
  <p class="caption abs" style="left:132px;top:866px">resurrection prayers video</p>
  <p class="post-body abs" style="left:54px;top:887px">In ultrices quo ut lectus, etiam vestibulum urna a est, pretium luctus euismod nisl, pellentesque turpis hac ridiculus massa. Venenatis a taciti dolor platea, curabitur lorem platea urna odio, convallis sit pellentesque lacus proin. Et ipsum velit diam nulla, fringilla vel tincidunt vitae, elit turpis tellus vivamus, dictum adipiscing convallis magna.</p>
  <a class="readmore abs" href="#" style="left:54px;top:944px">Read More</a>
  <div class="ribbon abs" style="left:382px;top:944px">Opportunities</div>
  <div class="ribbon-tail abs" style="left:520px;top:972px"></div>

  <nav class="pager abs" style="left:54px;top:1014px">
    <a href="#">First</a><a href="#">Previous</a><a class="current" href="#">1</a><a href="#">2</a><a href="#">3</a><a href="#">4</a><a href="#">Next</a><a href="#">Last</a>
  </nav>
  <span class="rss abs" style="left:480px;top:1014px"></span>
</main>

<aside>
  <section class="side abs" style="top:184px">
    <h3>About Hannah</h3>
    <div class="pic" role="img" aria-label="Profile photo placeholder" style="width:108px;height:102px"></div>
    <p>Lorem ipsum dolor sit amet, maiores ornare ac fermentum, imperdiet ut vivamus a, nam lectus at nunc. Quam euismod sem, semper ut potenti pellentesque quisque. In eget sapien sed, sit duis vestibulum ultricies, placerat morbi amet vel, nullam in inlorem vel. In molestie elit dui dictum, praesent nascetur pulvinar sed, in dolor pede in aliquam, risus nec error.</p>
    <a class="more" href="#">Read more...</a>
  </section>
  <section class="side abs" style="top:436px">
    <h3>About Hannah's Ministry</h3>
    <p>Lorem ipsum dolor sit amet, maiores ornare ac fermentum, imperdiet ut vivamus a, nam lectus at nunc. Quam euismod sem, semper ut potenti pellentesque quisque. In eget sapien sed, sit duis vestibulum ultricies, placerat morbi amet vel, nullam in inlorem vel. In molestie elit dui dictum, praesent nascetur pulvinar sed, in dolor pede in aliquam, risus nec error.</p>
    <a class="more" href="#">Read more...</a>
  </section>
  <section class="side abs" style="top:582px">
    <h3>About Malawi</h3>
    <div class="pic" role="img" aria-label="Map of Malawi" style="width:131px;height:89px;background:linear-gradient(135deg,#9a9a9a,#d8d48a 55%,#a9c98f)"></div>
    <p>Lorem ipsum dolor sit amet, maiores ornare ac fermentum, imperdiet ut vivamus a, nam lectus at nunc. Quam euismod sem, semper ut potenti pellentesque quisque. In eget sapien sed, sit duis vestibulum ultricies, placerat morbi amet vel, nullam in inlorem vel. In molestie elit dui dictum, praesent nascetur pulvinar sed, in dolor pede in aliquam, risus nec error.</p>
    <a class="more" href="#">Read more...</a>
  </section>
  <section class="side abs" style="top:829px">
    <h3>Harvest Reach Events</h3>
    <ul><li>Harvest Reach Prayer Event - May 15th</li><li>Harvest Reach Conference - June 30th</li></ul>
    <a class="more" href="#">Read more...</a>
  </section>
  <section class="side abs" style="top:917px">
    <h3>Harvest Reach Opportunities in Malawi</h3>
    <ul><li>- Teacher in Blanta (2yrs)</li><li>- Financial Controller (long term)</li><li>- Project Manager (6months+)</li><li>- Bible College Lecturer (long term)</li></ul>
    <a class="more" href="#">Read more...</a>
  </section>
</aside>

<footer>
  <div class="footer abs">
    <div class="col" style="left:15px"><h4>About FaithPostly</h4><ul><li><u>Mission Statement</u></li><li>Who We Are</li><li>History</li><li>Missionaries / Our Project]</li><li>Testimonials</li></ul></div>
    <div class="col" style="left:156px"><h4>Regions</h4><ul><li>Africa</li><li>Asia</li><li>North America</li><li>Latin America</li><li>Australia/Pacific</li></ul></div>
    <div class="col" style="left:256px"><h4>How You Can Suppport</h4><ul><li>Churches Partner</li><li>Mission Agencies</li><li>Mission Supporters</li><li>Mission Opportunities</li><li>Donation Opportunities</li></ul></div>
    <div class="col" style="left:418px"><h4>Mission Agencies</h4><ul><li>Lampstead</li><li>Wider Bridge</li><li>Harvest Reach Australia</li><li>Northwell Fellowship</li></ul></div>
    <div class="col" style="left:548px"><h4>Need Help ?</h4><ul><li>How it Works</li><li>Help/FAQ</li><li>Press / Announcement</li><li>Sitemap</li></ul></div>
    <div class="tab">Opportunities</div>
  </div>
  <span class="note abs" style="left:742px;top:1188px;font-size:9px">moveable box</span>
  <div class="legal abs" style="width:700px">
    <span class="mini"><i></i>faithpostly.org</span>
    <span>| Crossright © 2011 FaithPostly. Use of this website constitutes acceptance of our <a href="#" style="color:var(--red);text-decoration:none">Terms of Use</a> and <a href="#" style="color:var(--red);text-decoration:none">Privacy Policy</a>.</span>
  </div>
</footer>

</body>
</html>
```